Business card design for an Art Director working for museums

The business card design we're looking for is for an Art Director in a private museum called "OLV Gallery". The museum showcases artworks made by the country's national artists. Designs should use the CMYK "0 40 100 20". You have the liberty to use any type you want except for overly decorative ones.

Target Market(s)

Professional and creative individuals. Interior designers, museum curators, museum coordinators etc

Industry/Entity Type

Museum

Contact Information for Business Card

Rina T
Art Director
+1 555 374 9281

Font styles to use
Serif
Sans Serif
Script

Requirements
Must have
• My project must have the CMYK 0 40 100 20. You can play with the Key.
• We're keen on clean, minimal, and architectural-type design.
Nice to have
• Geometric gradients that nicely complement the main CMYK that we've posted.
Should not have
• Off-putting colour palettes

```html
<!DOCTYPE html>
<html lang="en">
<head>
<meta charset="utf-8">
<title>Rina T — Art Director Business Card</title>
<link rel="stylesheet" href="https://fonts.googleapis.com/css2?family=Playfair+Display:wght@700&family=Pinyon+Script&family=Open+Sans:wght@400&display=swap">
<style>
  :root {
    --backdrop: #d9d9d7;
    --card-white: #f6f6f4;
    --brand-amber: #cc7a00;
    --ink: #2b2b2b;
    --pattern-grey: #c9c9c7;
    --pattern-gold: #ead2a6;
  }
  * { margin: 0; padding: 0; box-sizing: border-box; }
  html, body {
    width: 1200px; height: 1000px; overflow: hidden;
    background: var(--backdrop);
  }
  .canvas {
    position: relative; width: 1200px; height: 1000px;
    display: flex; justify-content: center; align-items: center; gap: 100px;
  }
  .card {
    position: relative; width: 380px; height: 665px;
    box-shadow: 0 6px 18px rgba(0,0,0,0.18);
    overflow: hidden;
  }
  .card-front { background: var(--card-white); }
  .card-back {
    background: var(--brand-amber);
    display: flex; flex-direction: column; align-items: center; justify-content: center;
  }
  .brand-name {
    position: absolute; top: 110px; left: 60px;
    font-family: "Playfair Display", serif; font-weight: 700;
    font-size: 40px; letter-spacing: -1px; color: var(--ink);
  }
  .script-pattern {
    position: absolute; top: 190px; right: 0; width: 200px; height: 475px;
    background: linear-gradient(160deg, rgba(246,246,244,0) 0%, var(--pattern-grey) 35%, var(--pattern-gold) 60%, var(--pattern-grey) 85%, rgba(201,201,199,0.6) 100%);
    opacity: 0.7;
  }
  .job-title {
    position: absolute; left: 150px; top: 420px;
    transform: rotate(-90deg); transform-origin: left top;
    font-family: "Pinyon Script", cursive; font-size: 52px;
    color: var(--brand-amber); white-space: nowrap;
  }
  .phone-icon { width: 30px; height: 30px; margin-bottom: 8px; }
  .phone-number {
    font-family: "Open Sans", sans-serif; font-size: 17px; line-height: 1.45;
    color: var(--ink); text-align: center; list-style: none;
  }
</style>
</head>
<body>
<main class="canvas">
  <section class="card card-front" aria-label="Card front">
    <div class="script-pattern" role="img" aria-label="Layered handwritten 'Art Director' script pattern in grey and gold"></div>
    <h1 class="brand-name">Rina T</h1>
    <p class="job-title">Art Director</p>
  </section>
  <section class="card card-back" aria-label="Card back">
    <svg class="phone-icon" viewBox="0 0 24 24" aria-hidden="true">
      <path fill="#ffffff" d="M6.6 10.8a15.1 15.1 0 0 0 6.6 6.6l2.2-2.2a1 1 0 0 1 1-.25 11.4 11.4 0 0 0 3.6.57 1 1 0 0 1 1 1V20a1 1 0 0 1-1 1A17 17 0 0 1 3 4a1 1 0 0 1 1-1h3.5a1 1 0 0 1 1 1c0 1.25.2 2.45.57 3.57a1 1 0 0 1-.25 1z"/>
    </svg>
    <ul class="phone-number" aria-label="+1 555 374 9281">
      <li>+1</li>
      <li>555</li>
      <li>374</li>
      <li>92</li>
      <li>81</li>
    </ul>
  </section>
</main>
</body>
</html>
```